Web Design for an Online Dating Web Site

We need an uncoded web design for a new online dating web site called zMatchy.net. Simplicity and boldness are the key factors in the successful design.
Please look at the requirements document attached for details.
Updates
Dear all,
Please AVOID USING A PICTURE OF A HAPPY COUPLE ON THE HOME PAGE of the site. We highly want to move away from this space as it makes our web site just like another dating web site.
We like something simple with web 2.0 look and feel. The examples in the Requirements Document are exactly the design we are after.
Regards
Tarn
Industry/Entity Type
Dating
Look and feel
Each slider illustrates characteristics of the customer's brand and the style your logo design should communicate.

```html
<!DOCTYPE html>
<html lang="en">
<head>
<meta charset="utf-8">
<title>zMatchy.net – Why zMatchy?</title>
<link rel="stylesheet" href="https://fonts.googleapis.com/css2?family=Source+Sans+3:wght@400;600;700&display=swap">
<style>
  :root {
    --pink: #e0358f;
    --pink-dark: #c41f76;
    --pink-light: #ef6cb4;
    --grey-text: #8a8a8a;
    --sky: #1a8fdc;
    --sky-light: #3fb4f0;
    --white: #ffffff;
    --grass: #9ed51a;
    --grass-light: #b4e22a;
    --footer: #8cbc20;
    --footer-ink: #4d6b12;
    --frame-shadow: rgba(0, 30, 70, 0.45);
  }
  * { box-sizing: border-box; margin: 0; padding: 0; }
  html, body { width: 1200px; height: 670px; overflow: hidden; background: #e9e9e9; }
  body { font-family: "Source Sans 3", "Myriad Pro", Arial, sans-serif; position: relative; }

  .page { position: absolute; left: 5px; top: 0; width: 1190px; height: 668px; overflow: hidden; background: var(--white); }

  /* Header */
  .site-header { position: absolute; left: 0; top: 0; width: 100%; height: 108px; z-index: 3;
         background: var(--white); box-shadow: 0 3px 6px rgba(10, 79, 138, 0.35); }
  .brand { position: absolute; left: 160px; top: 14px; display: flex; align-items: center; gap: 8px; }
  .brand-dot { width: 16px; height: 16px; border-radius: 50%; background: var(--pink); }
  .brand-name { font-size: 40px; font-weight: 700; color: var(--pink); letter-spacing: -0.5px; line-height: 1; }

  .main-nav { position: absolute; left: 506px; top: 34px; display: flex; align-items: center; font-size: 15.5px; color: var(--grey-text); }
  .main-nav .home-icon { width: 20px; height: 18px; margin-right: 10px; }
  .main-nav a { color: var(--grey-text); text-decoration: none; }
  .main-nav .sep { margin: 0 8px; color: #a5a5a5; }

  .social-top { position: absolute; left: 943px; top: 34px; display: flex; gap: 5px; }
  .social-top span { width: 18px; height: 18px; border-radius: 3px; }
  .social-top .s1 { background: #3c63a8; }
  .social-top .s2 { background: #74bfe6; }
  .social-top .s3 { background: #d8d8d8; }
  .social-top .s4 { background: #f07c1c; }

  /* Sky */
  .sky { position: absolute; left: 0; top: 95px; width: 100%; height: 445px;
         background: linear-gradient(180deg, var(--sky) 0%, var(--sky) 60%, var(--sky-light) 100%); }
  .feature-band { position: absolute; left: 0; top: 165px; width: 100%; height: 340px;
         background: linear-gradient(90deg, #0a64b4 0%, #1381d3 45%, #1381d3 75%, #0a64b4 100%); }

  .slider-arrow { position: absolute; top: 290px; width: 48px; height: 90px; }
  .slider-arrow.prev { left: 25px; }
  .slider-arrow.next { left: 1120px; }

  .video-frame { position: absolute; left: 160px; top: 182px; width: 400px; height: 306px; background: var(--white);
         border-radius: 14px; box-shadow: 0 4px 10px var(--frame-shadow); }
  .video-still { position: absolute; left: 11px; top: 11px; width: 377px; height: 283px;
         background: linear-gradient(135deg, #8f8a74 0%, #b9a98a 35%, #7a5a3c 65%, #5d4a36 100%); }
  .play-button { position: absolute; left: 141px; top: 94px; width: 94px; height: 94px; }

  .feature-copy { position: absolute; left: 638px; top: 176px; width: 420px; color: var(--white); }
  .feature-copy h1 { font-size: 40px; font-weight: 700; line-height: 48px; }
  .feature-copy h2 { font-size: 17px; font-weight: 700; margin-top: 6px; letter-spacing: 0.2px; }
  .feature-copy p { font-size: 12.8px; line-height: 15.6px; margin-top: 20px; }
  .feature-copy p + p { margin-top: 15px; }

  .signup-button { position: absolute; left: 853px; top: 419px; width: 178px; height: 69px;
         border: 3px solid var(--white); border-radius: 9px;
         background: linear-gradient(180deg, var(--pink-light) 0%, var(--pink) 50%, var(--pink-dark) 100%);
         box-shadow: 0 3px 6px rgba(0,0,0,0.3);
         color: var(--white); font-size: 35px; font-weight: 700; text-align: center; line-height: 62px;
         text-decoration: none; }

  /* Ground */
  .ground { position: absolute; left: 0; top: 538px; width: 100%; height: 92px;
         background: linear-gradient(180deg, var(--grass-light) 0%, var(--grass) 100%); }

  .site-footer { position: absolute; left: 0; top: 630px; width: 100%; height: 38px; background: var(--footer); }
  .social-bottom { position: absolute; left: 160px; top: 6px; display: flex; gap: 9px; }
  .social-bottom span { width: 26px; height: 26px; border-radius: 4px; background: var(--footer-ink); }
  .footer-links { position: absolute; right: 160px; top: 9px; font-size: 15.5px; color: var(--footer-ink); display: flex; align-items: center; }
  .footer-links .footer-brand { font-weight: 700; font-size: 17px; margin: 0 6px; }
  .footer-links .sep { margin: 0 7px; }
  .footer-links a { color: var(--footer-ink); text-decoration: none; }
</style>
</head>
<body>
<div class="page">

  <div class="sky"></div>
  <div class="feature-band"></div>

  <header class="site-header">
    <div class="brand">
      <span class="brand-name">zMatchy</span>
      <span class="brand-dot"></span>
    </div>

    <nav class="main-nav">
      <svg class="home-icon" viewBox="0 0 20 18" aria-label="Home"><path fill="#e0358f" d="M10 1 L19 9 H16 V17 H12 V12 H8 V17 H4 V9 H1 Z"/></svg>
      <a href="#">Why zMatchy</a><span class="sep">|</span>
      <a href="#">How it works</a><span class="sep">|</span>
      <a href="#">Sign Up</a><span class="sep">|</span>
      <a href="#">Log in</a><span class="sep">|</span>
      <a href="#">About Us</a>
    </nav>

    <div class="social-top" aria-label="Social links">
      <span class="s1"></span><span class="s2"></span><span class="s3"></span><span class="s4"></span>
    </div>
  </header>

  <svg class="slider-arrow prev" viewBox="0 0 48 90" aria-label="Previous slide">
    <defs>
      <linearGradient id="arrowFadeL" x1="0" x2="1" y1="0" y2="0">
        <stop offset="0" stop-color="#ffffff"/><stop offset="1" stop-color="#ffffff" stop-opacity="0.1"/>
      </linearGradient>
    </defs>
    <polygon points="0,45 28,0 28,22 48,22 48,68 28,68 28,90" fill="url(#arrowFadeL)"/>
  </svg>
  <svg class="slider-arrow next" viewBox="0 0 48 90" aria-label="Next slide">
    <defs>
      <linearGradient id="arrowFadeR" x1="1" x2="0" y1="0" y2="0">
        <stop offset="0" stop-color="#ffffff"/><stop offset="1" stop-color="#ffffff" stop-opacity="0.1"/>
      </linearGradient>
    </defs>
    <polygon points="48,45 20,0 20,22 0,22 0,68 20,68 20,90" fill="url(#arrowFadeR)"/>
  </svg>

  <div class="video-frame">
    <div class="video-still" role="img" aria-label="Video still: a woman in a jacket and scarf outdoors in front of an old stone building">
      <svg class="play-button" viewBox="0 0 94 94" aria-label="Play video">
        <circle cx="47" cy="47" r="43" fill="rgba(0,0,0,0.15)" stroke="#ffffff" stroke-width="5"/>
        <polygon points="36,28 68,47 36,66" fill="#ffffff"/>
      </svg>
    </div>
  </div>

  <section class="feature-copy">
    <h1>Why zMatchy ?</h1>
    <h2>LOREM, IPSUM, DOLOR...</h2>
    <p>Lorem ipsum dolor sit amet, consectetur&nbsp; do eiusmod tempor incididunt<br>ut labore et Ut enim ad minim veniam, quis nostrud nisi ut aliquip ex ea...</p>
    <p>Lorem ipsum dolor sit amet, consectetur&nbsp; do eiusmod tempor incididunt<br>ut labore et Ut enim ad minim veniam, quis nostrud nisi ut aliquip ex ea<br>Lorem ipsum dolor sit amet, consectetur&nbsp; do eiusmod tempor incididunt<br>ut labore et Ut enim ad minim veniam, quis nostrud nisi ut aliquip ex ea</p>
  </section>

  <a class="signup-button" href="#">Sign Up !</a>

  <div class="ground"></div>

  <footer class="site-footer">
    <div class="social-bottom" aria-label="Social links">
      <span></span><span></span><span></span><span></span>
    </div>
    <div class="footer-links">
      <span>© 2011</span>
      <span class="footer-brand">zMatchy</span>
      <span class="sep">|</span><a href="#">Terms of use</a>
      <span class="sep">|</span><a href="#">Privacy police</a>
      <span class="sep">|</span><a href="#">Accessibility</a>
    </div>
  </footer>

</div>
</body>
</html>
```